new construction company branding

branding

Can I have a banner made so I can hang it as 1) branding my jobsite 2) advertisement

Target Market(s)

Commercial

Industry/Entity Type

Construction Trade

Font styles to use
Other font styles liked:
• Cinzel bold

Colors
EB3D1F
EC4F4E
F09395
F8D3D4
FCEDEE

Requirements
Must have
• Bright colors for advertisement
Nice to have
• 36”x48” canvas
Should not have
• To busy

```html
<!DOCTYPE html>
<html lang="en">
<head>
<meta charset="utf-8">
<title>Northbeam Builders – General Contractor Flyer</title>
<link href="https://fonts.googleapis.com/css2?family=Rubik:wght@400;500;600;700&display=swap" rel="stylesheet">
<style>
  :root{
    --red:#e3141b;
    --ink:#111111;
    --text:#2a2a2a;
    --footer-grey:#838383;
    --paper:#ffffff;
    --backdrop:#7a7a7a;
    --tile-bar:rgba(20,20,20,.82);
  }
  *{box-sizing:border-box;margin:0;padding:0}
  html,body{width:1200px;height:1200px;overflow:hidden}
  body{background:var(--backdrop);font-family:"Rubik",sans-serif;position:relative}

  .flyer{position:absolute;left:197px;top:30px;width:806px;height:1140px;background:var(--paper);
    box-shadow:0 10px 30px rgba(0,0,0,.35);overflow:hidden}

  .hero-photo{position:absolute;left:300px;top:0;width:506px;height:492px;
    background:linear-gradient(90deg,rgba(255,255,255,1) 0%,rgba(255,255,255,0) 28%),
               linear-gradient(160deg,#eef0f3 0%,#d9dde2 40%,#9aa9c4 65%,#c9ccd2 100%)}
  .hero-photo::after{content:"";position:absolute;left:0;right:0;bottom:0;height:90px;
    background:linear-gradient(180deg,rgba(255,255,255,0),rgba(255,255,255,.6))}

  .brand{position:absolute;left:44px;top:160px;display:flex;align-items:center;gap:10px;
    font-weight:600;font-size:24px;color:var(--ink);white-space:nowrap}
  .brand-mark{width:14px;height:14px;background:var(--red)}

  .headline{position:absolute;left:44px;top:234px;line-height:1}
  .headline-top{font-weight:700;font-size:32px;color:var(--ink)}
  .headline-main{font-weight:700;font-size:66px;color:var(--red);margin-top:2px;letter-spacing:.5px}
  .headline-sub{font-weight:700;font-size:49px;color:var(--red);margin-top:-2px}

  .section-title{position:absolute;left:44px;font-size:28px;font-weight:500;color:var(--ink)}
  .section-title span{color:var(--red)}
  .about-title{top:396px}
  .services-title{top:620px;left:41px}

  .about-text{position:absolute;left:44px;top:444px;width:292px;font-size:12.6px;line-height:16.2px;
    color:var(--text);text-align:justify}

  .services{position:absolute;left:44px;top:674px;width:300px;list-style:none}
  .service{position:relative;padding-left:27px;font-size:12.6px;line-height:16.4px;color:var(--text);
    text-align:justify;margin-bottom:15px}
  .service svg{position:absolute;left:0;top:1px}
  .service:not(:last-child)::before{content:"";position:absolute;left:7px;top:16px;bottom:-14px;
    width:1.5px;background:var(--red)}
  .service:last-child::before{content:"";position:absolute;left:7px;top:16px;height:40px;
    width:1.5px;background:var(--red)}

  .feature-kicker{position:absolute;left:393px;top:479px;font-size:17px;color:var(--red)}
  .feature-title{position:absolute;left:393px;top:502px;font-size:21.5px;font-weight:700;
    color:var(--ink);line-height:24px}

  .service-tile{position:absolute;width:169px;height:169px;overflow:hidden}
  .tile-photo{position:absolute;inset:0}
  .tile-label{position:absolute;left:0;right:0;bottom:10px;height:22px;background:var(--tile-bar);
    color:#fff;font-weight:600;font-size:12.5px;line-height:22px;text-align:center;letter-spacing:.2px}
  .tile-roof{left:393px;top:568px}
  .tile-roof .tile-photo{background:linear-gradient(160deg,#e9e5df 0%,#b9b6b2 45%,#3a4455 70%,#6a6b6e 100%)}
  .tile-plumb{left:580px;top:568px}
  .tile-plumb .tile-photo{background:linear-gradient(200deg,#f1f1f1 0%,#c9c3bc 45%,#6b7a8f 75%,#3e4350 100%)}
  .tile-kitchen{left:393px;top:752px}
  .tile-kitchen .tile-photo{background:linear-gradient(170deg,#efefef 0%,#9c9a98 40%,#6d2f2f 60%,#3d4354 100%)}
  .tile-electric{left:580px;top:752px}
  .tile-electric .tile-photo{background:linear-gradient(150deg,#c89a5a 0%,#8d8a86 35%,#d8d8da 60%,#2d3140 100%)}

  .feature-text{position:absolute;left:393px;top:928px;width:357px;font-size:12.6px;line-height:16.3px;
    color:var(--text);text-align:justify}

  .footer{position:absolute;left:0;top:1037px;width:806px;height:103px}
  .footer svg{position:absolute;inset:0}
  .footer-address{position:absolute;left:41px;top:20px;color:#fff;font-size:15.5px;line-height:22px;
    text-transform:uppercase}
  .footer-address strong{font-weight:600}
  .footer-contact{position:absolute;left:396px;top:21px;color:#fff;text-transform:uppercase;line-height:1}
  .footer-phone{font-size:31px;font-weight:400}
  .footer-phone strong{font-weight:700}
  .footer-web{font-size:23px;margin-top:6px}
</style>
</head>
<body>
<main class="flyer">
  <div class="hero-photo" role="img" aria-label="Contractor in blue overalls shaking hands with a homeowner in a bright white kitchen"></div>

  <div class="brand"><span class="brand-mark"></span>NORTHBEAM BUILDERS</div>

  <h1 class="headline">
    <div class="headline-top">NORTHBEAM</div>
    <div class="headline-main">GENERAL</div>
    <div class="headline-sub">CONTRACTOR</div>
  </h1>

  <h2 class="section-title about-title">ABOUT <span>US</span></h2>
  <p class="about-text">Lorem ipsum dolor sit amet, consectetur adipiscing elit. Quid autem habent admirationis, cum prope accesseris? An hoc usque quaque, aliter in vita? Non igitur de improbo, sed de callido improbo quaerimus, qualis Q. Nam quibus rebus efficiuntur voluptates, eae non sunt in potestate sapientis. Negare non possum. Huic mori optimum esse propter desperationem sapientiae, illi propter spem vivere. Quid enim me prohiberet Epicureum</p>

  <h2 class="section-title services-title">OUR <span>SERVICES</span></h2>
  <ul class="services">
    <li class="service"><svg width="15" height="15" viewBox="0 0 16 16"><circle cx="8" cy="8" r="8" fill="#e3141b"/><path d="M4.3 8.2l2.5 2.4 5-5" stroke="#fff" stroke-width="2" fill="none"/></svg>Lorem ipsum dolor sit amet, consectetur adipiscing elit. Quid autem habent admirationis, cum prope accesseris?</li>
    <li class="service"><svg width="15" height="15" viewBox="0 0 16 16"><circle cx="8" cy="8" r="8" fill="#e3141b"/><path d="M4.3 8.2l2.5 2.4 5-5" stroke="#fff" stroke-width="2" fill="none"/></svg>Varietates autem iniurasque fortunae facile veteres philosophorum praeceptis instituta vita superabat. Et quod est munus, quod opus sapientiae?</li>
    <li class="service"><svg width="15" height="15" viewBox="0 0 16 16"><circle cx="8" cy="8" r="8" fill="#e3141b"/><path d="M4.3 8.2l2.5 2.4 5-5" stroke="#fff" stroke-width="2" fill="none"/></svg>Duo Reges: constructio interrete. Quia nec honesto quic quam honestius nec turpi turpius. Tria genera bonorum</li>
    <li class="service"><svg width="15" height="15" viewBox="0 0 16 16"><circle cx="8" cy="8" r="8" fill="#e3141b"/><path d="M4.3 8.2l2.5 2.4 5-5" stroke="#fff" stroke-width="2" fill="none"/></svg>Verum tamen cum de rebus grandioribus dicas, ipsae res verba rapiunt; Hoc non est positum in nostra actione.</li>
    <li class="service"><svg width="15" height="15" viewBox="0 0 16 16"><circle cx="8" cy="8" r="8" fill="#e3141b"/><path d="M4.3 8.2l2.5 2.4 5-5" stroke="#fff" stroke-width="2" fill="none"/></svg>Equidem etiam Epicurum, in physicis quidem, Democriteum puto. Respondeat totidem verbis. Nemo igitur esse beatus potest. Consequens.</li>
  </ul>

  <p class="feature-kicker">NEQUE SOLUM EA COMMUNIA</p>
  <h3 class="feature-title">EST ENIM EFFECTR MULTARUM<br>ETRT MAGNARUM VOLUPTATUM.</h3>

  <figure class="service-tile tile-roof">
    <div class="tile-photo" role="img" aria-label="Roofer in hard hat and safety vest working on shingles"></div>
    <figcaption class="tile-label">TAMEN EXPETITUR</figcaption>
  </figure>
  <figure class="service-tile tile-plumb">
    <div class="tile-photo" role="img" aria-label="Plumber repairing pipes under a sink"></div>
    <figcaption class="tile-label">HONESTO QUIC</figcaption>
  </figure>
  <figure class="service-tile tile-kitchen">
    <div class="tile-photo" role="img" aria-label="Worker installing kitchen cabinets"></div>
    <figcaption class="tile-label">PUBLICA LIBRIS</figcaption>
  </figure>
  <figure class="service-tile tile-electric">
    <div class="tile-photo" role="img" aria-label="Electrician testing a breaker panel with a multimeter"></div>
    <figcaption class="tile-label">PRAESTARE VITAM</figcaption>
  </figure>

  <p class="feature-text">Lorem ipsum dolor sit amet, consectetur adipiscing elit. Quid autem habent admirationis, cum prope accesseris? An hoc usque quaque, aliter in vita? Non igitur de improbo, sed de callido improbo quaerimus, qualis Q. Nam quibus rebus efficiuntur voluptates,</p>

  <footer class="footer">
    <svg width="806" height="103" viewBox="0 0 806 103" aria-hidden="true">
      <polygon points="0,0 376,0 322,103 0,103" fill="#838383"/>
      <polygon points="386,0 806,0 806,103 332,103" fill="#e3141b"/>
    </svg>
    <div class="footer-address">
      <strong>NORTHBEAM BUILDERS LLC</strong><br>
      4120 RIDGELINE LANE<br>
      PINEHAVEN, OREGON 97410
    </div>
    <div class="footer-contact">
      <div class="footer-phone">CALL US <strong>555.014.2287</strong></div>
      <div class="footer-web">WWW.NORTHBEAMBUILDERS.COM</div>
    </div>
  </footer>
</main>
</body>
</html>
```